New Flyer Design Project - for sale units at The Lodge phase 3

on attached the A2 is full kitchen 1 bedroom, the A3 is gally kitchen and the B2 is the the 2 bedroom, on attached pictures the room with 2 queen beds is only for the 2 bedroom

This is going to be used to sale the units (real estate sale) so the layout could possibly be text and then pictures maybe 1 bedroom on one side and 2 on the back?

Experience the Modern Luxury of the New Phase 3 Building of the
Lodge at Harlow Bend

* Opening Spring 2019

* America's #17 Family Resort; Tennessee's Only Ranked Resort

1 Bedroom Bunk Suite (Galley Kitchen) - $199,000; Sleeps 6

* Private King Master Bedroom

* Bunk Bed Galley

* Granite Counters Throughout

* Fully Furnished with Custom Furnishings

* Private Balcony

* Equipped Galley Kitchen

* In Unit Laundry

* Queen Sleeper Sofa

1 Bedroom Bunk Suite (Full Kitchen) - $209,000; Sleeps 6

* Bunk Bed Galley

* Granite Counters throughout

* Equipped Full Kitchen

* Completely Furnished with Custom Furnishings

* Private Balcony

* In Unit Laundry

* Queen Sleeper Sofa

2 Bedroom Bunk Suite (Full Kitchen) - $249,000; Sleeps 10

* Private King Master Bedroom with On-Suite Bathroom

* Two Queen Bedroom

* Bunk Bed Galley

* Full Kitchen

* Private Balcony

* In Unit Laundry

* Queen Sleeper Sofa

Target Market(s)

people wanting to buy units in phase 3 of The Lodge at Harlow Bend

Industry/Entity Type

Real Estate Development

Requirements
Must have
• attached text to describe units and price
• pictures and layouts
• Contact Dale Porter
• 865-730-2958 Dale@brightfernretreats.example
Nice to have
• brand and logo
Should not have
• it should not be plain this is m ore of a luxury project

```html
<!DOCTYPE html>
<html lang="en">
<head>
<meta charset="utf-8">
<title>The Lodge at Harlow Bend – Phase 3 Sales Flyer</title>
<link rel="stylesheet" href="https://fonts.googleapis.com/css2?family=Montserrat:wght@500;600;700;800&display=swap">
<style>
  :root{
    --backdrop:#ececec;
    --paper:#ffffff;
    --orange:#d49a5a;
    --orange-deep:#b8743a;
    --teal:#3d6470;
    --teal-dark:#2f5059;
    --price:#1f6a86;
    --brown-text:#a8621c;
    --ink:#2b2b2b;
    --plan-bg:#ece6da;
  }
  *{box-sizing:border-box;margin:0;padding:0}
  html,body{width:1200px;height:776px;overflow:hidden;background:var(--backdrop);font-family:'Montserrat',sans-serif;color:var(--ink)}
  .sheet{position:absolute;top:20px;width:520px;height:736px;background:var(--paper);overflow:hidden;box-shadow:0 2px 10px rgba(0,0,0,.12)}
  .sheet--two-bed{left:50px}
  .sheet--one-bed{left:630px}
  .shape-layer{position:absolute;left:0;top:0}

  .brand{position:absolute;left:50%;transform:translateX(-50%);display:flex;align-items:center;gap:8px;padding:8px 14px;background:#8d8f91;white-space:nowrap}
  .brand__mark{width:10px;height:10px;background:var(--paper)}
  .brand__name{font-weight:700;font-size:13px;color:var(--paper);letter-spacing:.5px}

  .suite-pill{position:absolute;height:26px;background:var(--teal);color:#fff;font-weight:700;font-size:11px;letter-spacing:.3px;display:flex;align-items:center;justify-content:center;text-transform:uppercase;white-space:nowrap}
  .suite-pill--centered{left:110px;width:300px;border-radius:14px}
  .suite-pill--flush{left:0;width:290px;border-radius:0 14px 14px 0;padding-left:10px;justify-content:flex-start}
  .suite-pill--compact{left:0;width:275px;height:24px;font-size:10.5px;border-radius:0 13px 13px 0;padding-left:12px;justify-content:flex-start}

  .price{position:absolute;font-weight:700;font-size:20px;color:var(--price);white-space:nowrap}
  .price--compact{font-size:17px}
  .price__sign{font-size:13px;color:var(--ink);margin-right:2px}

  .floor-plan{position:absolute;border-radius:18px;background:linear-gradient(135deg,var(--plan-bg),#d8cdb9);border:3px solid #fff;box-shadow:0 2px 6px rgba(0,0,0,.25)}
  .plan-label{position:absolute;font-weight:700;font-size:13px;color:var(--ink)}

  .features{list-style:none;position:absolute}
  .features li{position:relative;padding-left:20px;font-weight:600;font-size:11.5px;line-height:1.25;margin-bottom:11px}
  .features--tight li{margin-bottom:7px;font-size:11px}
  .features--dense li{margin-bottom:6px;font-size:11px}
  .features--mini li{margin-bottom:5px;font-size:10.5px}
  .features li::before{content:"";position:absolute;left:0;top:2px;width:9px;height:9px;border:1px solid var(--orange);border-radius:50%}
  .features li::after{content:"";position:absolute;left:3px;top:4px;width:3px;height:5px;border:solid var(--orange);border-width:0 1.5px 1.5px 0;transform:rotate(45deg)}
  .features li:nth-child(even)::before{border-color:var(--teal)}
  .features li:nth-child(even)::after{border-color:var(--teal)}

  .backdrop-photo{position:absolute;left:0;top:400px;width:520px;height:280px;background:linear-gradient(180deg,rgba(255,255,255,0),rgba(214,214,214,.35) 60%,rgba(255,255,255,0))}

  .contact-bar{position:absolute;left:0;bottom:0;width:520px;height:44px;background:var(--teal);color:#fff;display:flex;align-items:center;gap:26px;padding-left:24px;font-size:10.5px;font-weight:500;white-space:nowrap}
  .contact-bar__phone{display:flex;align-items:center;gap:5px}
  .contact-accent{position:absolute;right:0;bottom:44px;width:110px;height:22px;background:var(--orange-deep);clip-path:polygon(18px 0,100% 0,100% 100%,0 100%)}

  .hero-photo{position:absolute;left:0;top:0;width:520px;height:215px;background:linear-gradient(120deg,#8a9a7a 0%,#e6e2d6 35%,#f4f1ea 55%,#6d6258 85%,#4e463f 100%)}
  .hero-title{position:absolute;left:0;width:520px;text-align:center;font-weight:800;color:var(--ink);text-transform:uppercase}
  .intro{position:absolute;left:40px;top:272px;width:440px;font-weight:700;font-size:11px;color:var(--brown-text);text-transform:uppercase;line-height:1.35}
</style>
</head>
<body>

<!-- Back side: two bedroom suite and one bedroom full kitchen -->
<section class="sheet sheet--two-bed">
  <div class="backdrop-photo" role="img" aria-label="Faded interior photo of a furnished dining area"></div>
  <svg class="shape-layer" width="520" height="170" viewBox="0 0 520 170">
    <polygon points="0,0 520,0 520,92 260,135 0,92" fill="var(--orange)"/>
    <polygon points="30,100 260,142 490,100 490,110 260,154 30,110" fill="var(--teal)"/>
  </svg>
  <div class="brand" style="top:36px"><span class="brand__mark"></span><span class="brand__name">The Lodge at Harlow Bend</span></div>

  <div class="suite-pill suite-pill--centered" style="top:172px">2. Bedroom Bunk Suite (Full Kitchen)</div>
  <div class="price" style="left:160px;top:204px"><span class="price__sign">$</span>249,000; Sleeps 10</div>

  <div class="floor-plan" style="left:18px;top:250px;width:215px;height:150px" role="img" aria-label="Floor plan A3, two bedroom full kitchen suite"></div>
  <div class="plan-label" style="left:110px;top:412px">(A3)</div>

  <ul class="features features--dense" style="left:250px;top:252px;width:255px">
    <li>Private King Master Bedroom with On-Suite Bathroom</li>
    <li>Two Queen Bedroom</li>
    <li>Bunk Bed Galley</li>
    <li>Granite Counters Throughout</li>
    <li>Full Kitchen</li>
    <li>Private Balcony</li>
    <li>In Unit Laundry</li>
    <li>Queen Sleeper Sofa</li>
  </ul>

  <div class="suite-pill suite-pill--compact" style="top:458px">1. Bedroom Bunk Suite (Full Kitchen)</div>
  <div class="price price--compact" style="left:30px;top:490px"><span class="price__sign">$</span>209,000; Sleeps 6</div>
  <ul class="features features--mini" style="left:30px;top:522px;width:265px">
    <li>Bunk Bed Galley</li>
    <li>Granite Counters Throughout</li>
    <li>Equipped Full Kitchen</li>
    <li>Completely Furnished with Custom Furnishings</li>
    <li>Private Balcony</li>
    <li>In Unit Laundry</li>
    <li>Queen Sleeper Sofa</li>
  </ul>

  <div class="floor-plan" style="left:310px;top:462px;width:190px;height:180px" role="img" aria-label="Floor plan B2, two bedroom suite"></div>
  <div class="plan-label" style="left:385px;top:650px">(B2)</div>

  <div class="contact-accent"></div>
  <footer class="contact-bar">
    <span class="contact-bar__phone">
      <svg width="10" height="10" viewBox="0 0 24 24"><path fill="#fff" d="M6.6 10.8a15 15 0 0 0 6.6 6.6l2.2-2.2a1 1 0 0 1 1-.25 11.4 11.4 0 0 0 3.6.57 1 1 0 0 1 1 1V20a1 1 0 0 1-1 1A17 17 0 0 1 3 4a1 1 0 0 1 1-1h3.5a1 1 0 0 1 1 1c0 1.25.2 2.45.57 3.6a1 1 0 0 1-.25 1z"/></svg>
      Contact- 865-730-2958 (Dale Porter)
    </span>
    <span>Email-Id - Dale@brightfernretreats.example</span>
  </footer>
</section>

<!-- Front side: one bedroom galley suite -->
<section class="sheet sheet--one-bed">
  <div class="hero-photo" role="img" aria-label="Photo of a bright suite bedroom with a made bed, window and bedside lamp"></div>
  <div class="brand" style="top:22px"><span class="brand__mark"></span><span class="brand__name">The Lodge at Harlow Bend</span></div>

  <svg class="shape-layer" width="520" height="270" viewBox="0 0 520 270">
    <polygon points="0,195 30,195 30,205 0,205" fill="var(--orange)"/>
    <polygon points="490,195 520,195 520,205 490,205" fill="var(--orange)"/>
    <polygon points="60,165 460,165 460,208 260,240 60,208" fill="var(--paper)"/>
    <polygon points="75,218 260,248 445,218 445,228 260,260 75,228" fill="var(--teal)"/>
  </svg>
  <div class="hero-title" style="top:174px;font-size:19px">Real Estate Development</div>
  <div class="hero-title" style="top:200px;font-size:16px">For Sale</div>

  <p class="intro">Experience the Modern Luxury of the New Phase 3 Building of the Lodge at Harlow Bend :</p>

  <ul class="features features--tight" style="left:30px;top:322px;width:260px">
    <li>Opening Spring 2019</li>
    <li>America's #17 Family Resort; Tennessee's Only Ranked Resort</li>
  </ul>

  <div class="suite-pill suite-pill--flush" style="top:392px">1. Bedroom Bunk Suite (Galley Kitchen)</div>
  <div class="price" style="left:30px;top:428px"><span class="price__sign">$</span>199,000; Sleeps 6</div>

  <ul class="features features--tight" style="left:36px;top:468px;width:270px">
    <li>Private King Master Bedroom</li>
    <li>Bunk Bed Galley</li>
    <li>Granite Counters Throughout</li>
    <li>Fully Furnished with Custom Furnishings</li>
    <li>Private Balcony</li>
    <li>Equipped Galley Kitchen</li>
    <li>In Unit Laundry</li>
    <li>Queen Sleeper Sofa</li>
  </ul>

  <div class="floor-plan" style="left:305px;top:312px;width:200px;height:235px" role="img" aria-label="Floor plan A2, one bedroom galley kitchen suite"></div>
  <div class="plan-label" style="left:390px;top:558px">(A2)</div>

  <div class="contact-accent"></div>
  <footer class="contact-bar">
    <span class="contact-bar__phone">
      <svg width="10" height="10" viewBox="0 0 24 24"><path fill="#fff" d="M6.6 10.8a15 15 0 0 0 6.6 6.6l2.2-2.2a1 1 0 0 1 1-.25 11.4 11.4 0 0 0 3.6.57 1 1 0 0 1 1 1V20a1 1 0 0 1-1 1A17 17 0 0 1 3 4a1 1 0 0 1 1-1h3.5a1 1 0 0 1 1 1c0 1.25.2 2.45.57 3.6a1 1 0 0 1-.25 1z"/></svg>
      Contact- 865-730-2958 (Dale Porter)
    </span>
    <span>Email-Id - Dale@brightfernretreats.example</span>
  </footer>
</section>

</body>
</html>
```